Business card for a vending machine business

I need a business card for my vending machine business. The name is Kestrel Snackworks, LLC. The card is one-sided, and landscape format. Not portrait.

The information for the card is as follows:

Dana Whitlow
Owner
(555) 314-2907
Kestrelsnackworks.example
Info@kestrelsnackworks.example

I'd like colors and design elements to match what's in my logo and company name. I'd like to have the checkered flag or racing stripe if possible You can use a border if youd like. You can use a background color if it looks nice and doesn't clash with the logo
Use your creativity. But a white background is perfectly fine. The card can be as simple, yet gets the point across to match the company name and logo.

I uploaded a copy of my logo. I also uploaded a businesses card I started to create, but since it was missing something, I gave up. Another upload has a red thunderbolt and the checkerer flag. Those two uploads are for inspiration. Again, please make sure to make the card landscape, not portrait. Thank you, designers. Good luck to all.

```html
<!DOCTYPE html>
<html lang="en">
<head>
<meta charset="UTF-8">
<title>Kestrel Snackworks – Business Card</title>
<link href="https://fonts.googleapis.com/css2?family=Poppins:wght@600;700;800&display=swap" rel="stylesheet">
<style>
  :root {
    --race-red: #ff0000;
    --deep-red: #c80000;
    --ink: #0a0a0a;
    --paper: #ffffff;
    --stage: #e6e6e6;
    --machine-blue: #1f7fa8;
    --machine-light: #dfe9ee;
  }
  * { box-sizing: border-box; margin: 0; padding: 0; }
  html, body {
    width: 1200px; height: 1200px; overflow: hidden;
    background: var(--stage);
    font-family: "Poppins", sans-serif;
    color: var(--ink);
  }
  .sheet {
    width: 1200px; height: 1200px;
    display: flex; flex-direction: column; align-items: center; justify-content: center;
    gap: 26px;
  }
  .card {
    position: relative;
    width: 960px; height: 563px;
    border-radius: 22px;
    overflow: hidden;
  }

  /* Front */
  .card-front {
    background: linear-gradient(135deg, var(--race-red) 0%, #7a0000 50%, var(--race-red) 100%);
  }
  .front-mascot {
    position: absolute;
    left: 300px; top: 48px;
    width: 330px; height: 280px;
    border-radius: 40px 40px 16px 16px;
    background: linear-gradient(160deg, var(--machine-light) 0%, var(--machine-blue) 100%);
    border: 8px solid var(--paper);
  }
  .front-name {
    position: absolute;
    left: 0; right: 0; top: 345px;
    text-align: center;
    font-weight: 800;
    font-size: 62px;
    line-height: 1.05;
    color: var(--paper);
    text-transform: uppercase;
    letter-spacing: 1px;
  }

  /* Back */
  .card-back { background: var(--paper); }
  .side-stripe {
    position: absolute; left: 0; top: 0; bottom: 0;
    width: 80px;
    background: linear-gradient(180deg, var(--race-red) 0%, #500000 50%, var(--race-red) 100%);
  }
  .brand-name {
    position: absolute;
    left: 122px; top: 52px;
    font-weight: 800;
    font-size: 46px;
    line-height: 1.05;
    color: var(--deep-red);
    text-transform: uppercase;
  }
  .person {
    position: absolute; left: 122px; top: 232px;
    text-transform: uppercase;
  }
  .person-name { font-weight: 800; font-size: 50px; line-height: 1.05; letter-spacing: 0.5px; }
  .person-role { font-weight: 800; font-size: 40px; line-height: 1.1; }
  .contact {
    position: absolute; left: 122px; top: 378px;
    list-style: none;
    display: flex; flex-direction: column; gap: 6px;
  }
  .contact-item { display: flex; align-items: center; gap: 10px; font-weight: 700; }
  .contact-phone { font-size: 40px; line-height: 1.15; }
  .contact-line { font-size: 24px; line-height: 1.35; }
  .contact-icon { flex: none; }
  .back-mascot {
    position: absolute;
    right: 0; bottom: 0;
    width: 340px; height: 440px;
    border-top-left-radius: 60px;
    background: linear-gradient(160deg, #f4f4f4 0%, var(--machine-blue) 100%);
  }
</style>
</head>
<body>
  <main class="sheet">
    <section class="card card-front" aria-label="Card front">
      <div class="checker-field" role="img" aria-label="Red and black checkered pattern background" style="position:absolute;inset:0;"></div>
      <div class="front-mascot" role="img" aria-label="Cartoon vending machine mascot waving a checkered racing flag"></div>
      <p class="front-name">Kestrel<br>Snackworks</p>
    </section>

    <section class="card card-back" aria-label="Card back">
      <div class="side-stripe" role="img" aria-label="Vertical red and black checkered stripe"></div>
      <p class="brand-name">Kestrel<br>Snackworks</p>
      <div class="person">
        <p class="person-name">Dana Whitlow</p>
        <p class="person-role">Owner</p>
      </div>
      <ul class="contact">
        <li class="contact-item contact-phone">
          <svg class="contact-icon" width="34" height="34" viewBox="0 0 24 24" aria-hidden="true"><path fill="#0a0a0a" d="M6.6 10.8c1.4 2.8 3.8 5.1 6.6 6.6l2.2-2.2c.3-.3.7-.4 1-.2 1.1.4 2.3.6 3.6.6.6 0 1 .4 1 1V20c0 .6-.4 1-1 1C10.6 21 3 13.4 3 4c0-.6.4-1 1-1h3.5c.6 0 1 .4 1 1 0 1.3.2 2.5.6 3.6.1.3 0 .7-.2 1z"/></svg>
          (555) 314-2907
        </li>
        <li class="contact-item contact-line">
          <svg class="contact-icon" width="26" height="20" viewBox="0 0 26 20" aria-hidden="true"><rect x="1" y="1" width="24" height="18" fill="#0a0a0a"/><path d="M2 2l11 9 11-9M2 18l8-7M24 18l-8-7" stroke="#fff" stroke-width="2" fill="none"/></svg>
          Info@kestrelsnackworks.example
        </li>
        <li class="contact-item contact-line">
          <svg class="contact-icon" width="26" height="26" viewBox="0 0 24 24" aria-hidden="true"><g fill="none" stroke="#0a0a0a" stroke-width="2"><circle cx="12" cy="12" r="10"/><ellipse cx="12" cy="12" rx="4" ry="10"/><path d="M2 12h20M4 6.5h16M4 17.5h16"/></g></svg>
          Kestrelsnackworks.example
        </li>
      </ul>
      <div class="back-mascot" role="img" aria-label="Cartoon vending machine mascot holding a checkered racing flag"></div>
    </section>
  </main>
</body>
</html>
```